Business Card for: Keelwright Financial Advisory Services Inc.

provide strategic financial advisory services to companies in the areas of corporate finance, mergers and acquisitions, executive coaching and strategic planning

Target Market(s)

Companies, banks, accountants, lawyers

Industry/Entity Type

High end business consulting in corporate finance, mergers and acquisitions, consulting

Contact Information for Business Card

Name of company, Name: xxxxxx xxxxxx , CEO, - phone number: 1-xxx-xxx-xxxx, - email address,

Requirements
Must have
• Must be professional and simple.
Nice to have
• simple, straight graphics, must give the impression that we are trustworthy, professional, competent
Should not have
• loud colors, loud design features

```html
<!DOCTYPE html>
<html lang="en">
<head>
<meta charset="utf-8">
<title>Keelwright Financial Advisory Services Inc. – Business Card</title>
<link rel="stylesheet" href="https://fonts.googleapis.com/css2?family=Poppins:wght@400;500;700&display=swap">
<style>
  :root {
    --backdrop: #1c1c21;
    --card: #232527;
    --accent: #f48a1a;
    --ink-light: #e9e9e9;
    --ink-muted: #c9c9c9;
  }
  * { margin: 0; padding: 0; box-sizing: border-box; }
  html, body {
    width: 1200px;
    height: 801px;
    overflow: hidden;
    background: var(--backdrop);
    font-family: "Poppins", sans-serif;
  }
  .canvas {
    width: 1200px;
    height: 801px;
    display: flex;
    align-items: center;
    justify-content: center;
    gap: 40px;
  }
  .card {
    position: relative;
    width: 540px;
    height: 309px;
    background: var(--card);
    box-shadow: 0 18px 40px rgba(0, 0, 0, 0.55);
    overflow: hidden;
  }

  /* Front */
  .card-front {
    display: flex;
    align-items: center;
    justify-content: center;
  }
  .wordmark {
    display: flex;
    flex-direction: column;
    align-items: flex-start;
  }
  .wordmark-name {
    color: var(--accent);
    font-weight: 700;
    font-size: 58px;
    line-height: 1;
    letter-spacing: 0.5px;
  }
  .wordmark-tagline {
    color: var(--accent);
    font-weight: 500;
    font-size: 14px;
    letter-spacing: 1.6px;
    margin-top: 6px;
    margin-left: 4px;
  }

  /* Back */
  .card-back .wordmark {
    position: absolute;
    left: 44px;
    top: 58px;
  }
  .card-back .wordmark-name { font-size: 42px; }
  .card-back .wordmark-tagline { font-size: 11px; letter-spacing: 1.3px; margin-top: 4px; }

  .contact-person {
    position: absolute;
    left: 112px;
    top: 150px;
  }
  .person-name {
    color: var(--accent);
    font-weight: 700;
    font-size: 22px;
    line-height: 1.1;
  }
  .person-role {
    color: var(--ink-light);
    font-size: 12px;
    letter-spacing: 1px;
    margin-top: 2px;
    padding-bottom: 6px;
    border-bottom: 2px solid var(--accent);
    width: 72px;
  }
  .contact-list {
    position: absolute;
    left: 130px;
    top: 222px;
    list-style: none;
  }
  .contact-item {
    display: flex;
    align-items: center;
    gap: 10px;
    color: var(--ink-muted);
    font-size: 13px;
    line-height: 24px;
  }
  .contact-icon { width: 14px; height: 14px; flex: none; }
  .accent-band {
    position: absolute;
    left: 0;
    right: 0;
    bottom: 0;
    height: 6px;
    background: var(--accent);
  }
</style>
</head>
<body>
<main class="canvas">
  <section class="card card-front" aria-label="Business card front">
    <div class="wordmark">
      <span class="wordmark-name">Keelwright</span>
      <span class="wordmark-tagline">Financial Advisory Services Inc.</span>
    </div>
  </section>

  <section class="card card-back" aria-label="Business card back">
    <div class="wordmark">
      <span class="wordmark-name">Keelwright</span>
      <span class="wordmark-tagline">Financial Advisory Services Inc.</span>
    </div>

    <div class="contact-person">
      <p class="person-name">Marcus R Hale</p>
      <p class="person-role">CEO</p>
    </div>

    <ul class="contact-list">
      <li class="contact-item">
        <svg class="contact-icon" viewBox="0 0 24 24" aria-hidden="true">
          <path fill="var(--accent)" d="M6.6 10.8a15.1 15.1 0 0 0 6.6 6.6l2.2-2.2a1 1 0 0 1 1-.25 11.4 11.4 0 0 0 3.6.57 1 1 0 0 1 1 1V20a1 1 0 0 1-1 1A17 17 0 0 1 3 4a1 1 0 0 1 1-1h3.5a1 1 0 0 1 1 1c0 1.25.2 2.45.57 3.57a1 1 0 0 1-.25 1z"/>
        </svg>
        <span>1-555-214-0386</span>
      </li>
      <li class="contact-item">
        <svg class="contact-icon" viewBox="0 0 24 24" aria-hidden="true">
          <rect x="2" y="5" width="20" height="14" fill="var(--accent)"/>
          <path d="M2 5l10 8 10-8" fill="none" stroke="var(--card)" stroke-width="1.6"/>
        </svg>
        <span>info@keelwrightadvisory.com</span>
      </li>
    </ul>

    <div class="accent-band"></div>
  </section>
</main>
</body>
</html>
```